Bright Meadow Counseling Business Card design with a visually interesting use of Space

I need business cards that are luxurious and give a peaceful, calm vibe. I also had some letterhead designed, and i like the look of it also, it's attached with the logo design for reference/ ideas but feel free to be creative.

Target Market(s)

High end luxurious client who needs counseling

Industry/Entity Type

Marriage and Family Therapy

Contact Information for Business Card

Mira Kowalczyk MS LMFT/ or Toby Hallett address 4150 Larkin Suite 600

Font styles to use
Sans Serif

Colors
0054AA
0677BA
7BADD7
CADEEF
E8F1F8
0094D4
00A9DD
6FCCEA
C7EBF8
E9F6FB
A7469A
B969AE
D3A5CF
EDDBEB
F8F0F9
6B429C
8869AF
B7A5CE
E3DAEB
F3F0F8

Requirements
Must have
• Logo and color scheme but be simple modern and luxurious
Nice to have
• I'd like to incorporate some elelmets from the logo and letterhead into a simple modern card

```html
<!DOCTYPE html>
<html lang="en">
<head>
<meta charset="utf-8">
<title>Bright Meadow Counseling – Business Card</title>
<link href="https://fonts.googleapis.com/css2?family=Jost:wght@200;300;400&display=swap" rel="stylesheet">
<style>
  :root {
    --backdrop: #2e2e2e;
    --card-white: #ffffff;
    --card-black: #1c1c1c;
    --ink-light: #ffffff;
    --emboss: #9a9a9a;
    --sky: #6fccea;
    --teal: #5cc3bd;
    --blue: #0677ba;
    --violet: #6b429c;
    --orchid: #a7469a;
    --rose: #b969ae;
  }
  * { margin: 0; padding: 0; box-sizing: border-box; }
  html, body {
    width: 1200px;
    height: 689px;
    overflow: hidden;
    background: var(--backdrop);
    font-family: "Jost", "Futura", sans-serif;
  }
  .stage {
    position: relative;
    width: 1200px;
    height: 689px;
  }
  .card {
    position: absolute;
    top: 196px;
    width: 520px;
    height: 297px;
    overflow: hidden;
    box-shadow: 0 18px 40px rgba(0, 0, 0, 0.45);
  }
  .card--front { left: 50px; background: var(--card-white); }
  .card--back  { left: 630px; background: var(--card-black); }

  .bubble-field {
    position: absolute;
    left: 40px;
    top: 28px;
    width: 420px;
    height: 260px;
    border-radius: 50%;
    background:
      radial-gradient(circle at 25% 25%, var(--sky) 0%, transparent 45%),
      radial-gradient(circle at 80% 75%, var(--rose) 0%, transparent 50%),
      radial-gradient(circle at 70% 25%, var(--teal) 0%, transparent 40%),
      radial-gradient(circle at 45% 55%, var(--violet) 0%, var(--orchid) 90%);
    opacity: 0.9;
  }
  .contact {
    position: absolute;
    left: 150px;
    top: 76px;
    width: 250px;
    color: var(--ink-light);
  }
  .contact__name {
    font-weight: 400;
    font-size: 21px;
    letter-spacing: 0.5px;
    text-transform: uppercase;
    white-space: nowrap;
  }
  .contact__title {
    font-weight: 300;
    font-size: 12px;
    margin-top: 2px;
    margin-left: 4px;
    white-space: nowrap;
  }
  .contact__icons {
    display: flex;
    gap: 8px;
    margin: 9px 0 7px 60px;
  }
  .contact__icons svg { width: 9px; height: 9px; }
  .contact__line {
    font-weight: 300;
    font-size: 11.5px;
    line-height: 1.45;
    white-space: nowrap;
  }

  .brand {
    position: absolute;
    left: 70px;
    top: 100px;
    color: var(--emboss);
    font-weight: 200;
  }
  .brand__name {
    font-size: 44px;
    letter-spacing: 1px;
    line-height: 1;
    white-space: nowrap;
  }
  .brand__sub {
    font-size: 18px;
    letter-spacing: 7px;
    margin: 8px 0 0 110px;
  }
  .brand__dot {
    position: absolute;
    left: 405px;
    top: 96px;
    width: 52px;
    height: 52px;
    border-radius: 50%;
    background: var(--violet);
  }
</style>
</head>
<body>
<main class="stage">
  <section class="card card--front">
    <div class="bubble-field" role="img" aria-label="Cluster of overlapping translucent circles in blue, teal, violet and rose"></div>
    <div class="contact">
      <h1 class="contact__name">Mira Kowalczyk</h1>
      <p class="contact__title">Behavioral Health Therapist</p>
      <div class="contact__icons" aria-hidden="true">
        <svg viewBox="0 0 10 10"><path d="M5 0.5a3 3 0 0 1 3 3c0 2.2-3 6-3 6s-3-3.8-3-6a3 3 0 0 1 3-3z" fill="#fff"/><circle cx="5" cy="3.5" r="1" fill="#8a4ba4"/></svg>
        <svg viewBox="0 0 10 10"><path d="M2 0.8l2 2-1 1.2a6 6 0 0 0 3 3l1.2-1 2 2-1.3 1.3C4.6 9 1 5.4 0.7 2.1z" fill="#fff"/></svg>
        <svg viewBox="0 0 10 10"><rect x="0.5" y="2" width="9" height="6" fill="#fff"/><path d="M0.5 2l4.5 3.5L9.5 2" stroke="#8a4ba4" stroke-width="0.8" fill="none"/></svg>
        <svg viewBox="0 0 10 10"><circle cx="5" cy="5" r="4.3" fill="none" stroke="#fff" stroke-width="1"/><ellipse cx="5" cy="5" rx="1.8" ry="4.3" fill="none" stroke="#fff" stroke-width="0.8"/><path d="M0.7 5h8.6" stroke="#fff" stroke-width="0.8"/></svg>
      </div>
      <p class="contact__line">4150 Larkin Suite 600, Hollis Vale 00412</p>
      <p class="contact__line">555.014.2290</p>
      <p class="contact__line">mira@BrightMeadowCounseling.com</p>
      <p class="contact__line">BrightMeadowCounseling.com</p>
    </div>
  </section>

  <section class="card card--back">
    <div class="brand">
      <p class="brand__name">Bright Meadow</p>
      <p class="brand__sub">Counseling</p>
    </div>
    <span class="brand__dot" aria-hidden="true"></span>
  </section>
</main>
</body>
</html>
```